QUILLO Q

we need a label for a polyacetate bag. The product is a disposable multi use cloth. These normally come in packs of 5- 10, we want to provide a greater quantity. So that the QUILLO refers to the quantity of cloths and not the size of the cloth. We want to bring excitement to an old and boring product.
The label size: 7 inches across x 9 inches long ( subject to bag manufacture's approval)
Colours : No more than 3
Name of the item is: QUILLO PAK
The number in each pack is : 50 ( This number should appear on the label)
The words: Re-useable, Multi-Purpose, Super Absorbent Cloths; KEEP OUT OF THE REACH OF CHILDREN, must appear on the label.
DIMENSIONS: 21X 14" ( 53cm X 35cm )
The label should not be totally occlusive, the cloth must be seen through clear parts of the label. Consequently the colours of the cloths, Blue, Pink or Green should be taken into account when making the choice of colors and quantity of color/ink needed for the label.
The efficient use of color and the quantity of ink required for the design is important. The cost to print the label must not exceed the value of this product.

```html
<!DOCTYPE html>
<html lang="en">
<head>
<meta charset="utf-8">
<title>QUILLO PAK label</title>
<link rel="stylesheet" href="https://fonts.googleapis.com/css2?family=Archivo:wght@800&family=Archivo+Narrow:wght@500&family=Open+Sans:wght@700&display=swap">
<style>
  :root {
    --ink: #231f20;
    --paper: #ffffff;
    --trim: #8cd05a;
  }
  html, body {
    margin: 0;
    padding: 0;
    width: 1200px;
    height: 1091px;
    overflow: hidden;
    background: var(--paper);
  }
  .canvas {
    position: relative;
    width: 1200px;
    height: 1091px;
    background: var(--paper);
  }
  .label-art {
    position: absolute;
    inset: 0;
  }
  .trim-line { fill: none; stroke: var(--trim); stroke-width: 1.5; }
  .ink-shape { fill: var(--ink); }
  .brand-name {
    position: absolute;
    left: 335px;
    top: 392px;
    margin: 0;
    font-family: "Archivo", sans-serif;
    font-weight: 800;
    font-size: 128px;
    line-height: 1;
    letter-spacing: 2px;
    color: var(--ink);
    white-space: nowrap;
  }
  .tagline {
    position: absolute;
    left: 177px;
    top: 700px;
    margin: 0;
    font-family: "Archivo Narrow", sans-serif;
    font-weight: 500;
    font-size: 38px;
    line-height: 1;
    color: var(--ink);
    white-space: nowrap;
    transform-origin: left bottom;
    transform: rotate(-13.5deg);
  }
  .count {
    position: absolute;
    left: 912px;
    top: 770px;
    width: 140px;
    text-align: center;
    color: var(--paper);
    font-family: "Archivo Narrow", sans-serif;
    font-weight: 500;
    line-height: 1;
  }
  .count-number { display: block; font-size: 78px; }
  .count-unit { display: block; font-size: 27px; margin-top: 2px; }
  .safety-warning {
    position: absolute;
    left: 161px;
    top: 872px;
    margin: 0;
    font-family: "Open Sans", sans-serif;
    font-weight: 700;
    font-size: 20px;
    color: var(--ink);
    white-space: nowrap;
  }
</style>
</head>
<body>
<div class="canvas">
  <svg class="label-art" width="1200" height="1091" viewBox="0 0 1200 1091" aria-hidden="true">
    <rect class="trim-line" x="110" y="165" width="973" height="756"/>
    <path class="ink-shape corner-top" d="M162 210 L662 210 Q360 275 162 505 Z"/>
    <path class="ink-shape swoosh-main" d="M143 790 Q580 660 1035 570 Q600 682 143 790 Z"/>
    <path class="ink-shape swoosh-lower" d="M210 802 Q620 702 1000 644 Q620 712 210 802 Z"/>
    <path class="ink-shape corner-bottom" d="M1050 683 L1050 891 L765 891 Z"/>
  </svg>

  <h1 class="brand-name">QUILLO Q</h1>
  <p class="tagline">Re-useable, Multi-Purpose, Super Absorbent Cloths</p>

  <div class="count">
    <span class="count-number">50</span>
    <span class="count-unit">TOWELS</span>
  </div>

  <p class="safety-warning">KEEP OUT OF THE REACH OF CHILDREN</p>
</div>
</body>
</html>
```